Local Horticulturalist needs Business card design

Meridel Horticulture would like to update our existing business card and utilize our new logo (design attached)....we specialize in getting the best out of our customers yard with professional maintenance programs, expert pruning and hedging and garden restorations.
Utilizing colors from attached logo I would like a design that implies professionalism and if possible our businesses love of restoration through plants.
I also sometimes write down for my customers a start date and price on the back of my current card
Target Market(s)
Home owners
Contractors
Industry/Entity Type
Gardener
Contact Information for Business Card
Gareth Volkstrom | Horticulturalist
ph: 0438275946
meridelhort@fernmail.example
www.meridelhorticulture.example.au
Requirements
Must have
- crucial information easy to read
- incorporate current logo
- Horticulturalist listed preferably near name
Nice to have
- currently I write a job start date and price on the back of my current card so something that integrates this would be beneficial
Should not have
- be pretty or flowerey
- be too white or basic

```html
<!DOCTYPE html>
<html lang="en">
<head>
<meta charset="utf-8">
<title>Meridel Horticulture – Business Card</title>
<link rel="stylesheet" href="https://fonts.googleapis.com/css2?family=Source+Sans+3:wght@400;600;700&display=swap">
<style>
  :root {
    --backdrop: #e6e6e6;
    --card-black: #161616;
    --card-black-soft: #222222;
    --leaf-green: #6cab2f;
    --earth-grey: #7b7266;
    --paper: #f6f6f5;
    --label-grey: #8a8a8a;
    --text-dark: #3a3a3a;
  }
  * { box-sizing: border-box; margin: 0; padding: 0; }
  html, body {
    width: 1200px; height: 726px; overflow: hidden;
    background: var(--backdrop);
    font-family: "Source Sans 3", "Myriad Pro", Arial, sans-serif;
  }
  .stage {
    position: relative; width: 1200px; height: 726px;
    display: flex; align-items: center; justify-content: center; gap: 44px;
  }
  .card {
    position: relative; width: 520px; height: 298px; overflow: hidden;
    border-radius: 3px;
    box-shadow: 0 6px 18px rgba(0,0,0,0.18);
  }

  /* Back of card */
  .card-back { background: linear-gradient(160deg, var(--card-black-soft), var(--card-black)); }
  .card-back .brand {
    position: absolute; left: 0; right: 0; top: 62px;
    display: flex; flex-direction: column; align-items: center; gap: 4px;
  }
  .brand-row { display: flex; align-items: center; gap: 12px; }
  .brand-dot {
    width: 30px; height: 30px; border-radius: 50%; background: var(--leaf-green);
  }
  .brand-name {
    font-weight: 700; font-size: 38px; letter-spacing: 0.5px; color: var(--leaf-green);
    line-height: 1;
  }
  .brand-tagline {
    font-weight: 600; font-size: 17px; letter-spacing: 1.5px; color: var(--earth-grey);
  }
  .job-field {
    position: absolute; left: 0; right: 0; top: 206px; height: 48px;
    background: var(--paper);
    display: flex; align-items: center;
    font-size: 15px; color: var(--label-grey);
  }
  .job-field .label-price { position: absolute; left: 30px; }
  .job-field .label-date  { position: absolute; left: 280px; }
  .job-divider {
    position: absolute; left: 0; right: 0; top: 198px; height: 3px; background: var(--paper);
  }

  /* Front of card */
  .card-front { background: var(--paper); }
  .card-front svg.panel { position: absolute; inset: 0; }
  .front-brand {
    position: absolute; left: 228px; top: 34px;
  }
  .front-brand .brand-name { font-size: 26px; }
  .front-brand .brand-tagline { font-size: 12px; letter-spacing: 1px; margin-top: 2px; }
  .person { position: absolute; left: 228px; top: 118px; }
  .person-name { font-weight: 700; font-size: 18px; color: var(--leaf-green); line-height: 1.1; }
  .person-role { font-size: 11px; color: var(--text-dark); margin-top: 2px; }
  .contacts {
    position: absolute; left: 228px; top: 176px; list-style: none;
    font-size: 13px; color: var(--text-dark);
  }
  .contacts li { display: flex; align-items: center; gap: 9px; height: 20px; }
  .contacts svg { width: 12px; height: 12px; fill: var(--earth-grey); flex: none; }
</style>
</head>
<body>
<main class="stage">

  <section class="card card-back" aria-label="Back of business card">
    <div class="brand">
      <div class="brand-row">
        <span class="brand-dot"></span>
        <span class="brand-name">Meridel Horticulture</span>
      </div>
      <span class="brand-tagline">Garden Restorations &amp; Maintenance</span>
    </div>
    <div class="job-divider"></div>
    <div class="job-field">
      <span class="label-price">Price</span>
      <span class="label-date">Date</span>
    </div>
  </section>

  <section class="card card-front" aria-label="Front of business card">
    <svg class="panel" viewBox="0 0 520 298" width="520" height="298">
      <path d="M0 0 H152 C205 70 176 200 206 298 H0 Z" fill="var(--earth-grey)"/>
      <path d="M0 0 H146 C199 70 170 200 200 298 H0 Z" fill="var(--leaf-green)"/>
      <path d="M0 0 H140 C193 70 164 200 194 298 H0 Z" fill="var(--card-black)"/>
    </svg>
    <div class="front-brand">
      <div class="brand-name">Meridel Horticulture</div>
      <div class="brand-tagline">Garden Restorations &amp; Maintenance</div>
    </div>
    <div class="person">
      <div class="person-name">Gareth Volkstrom</div>
      <div class="person-role">Horticulturalist</div>
    </div>
    <ul class="contacts">
      <li>
        <svg viewBox="0 0 12 12" aria-hidden="true"><path d="M1 4 C1 2 3 1 6 1 C9 1 11 2 11 4 L9 5 L8 3.5 H4 L3 5 Z M3 6 H9 L10 11 H2 Z"/></svg>
        0438275946
      </li>
      <li>
        <svg viewBox="0 0 12 12" aria-hidden="true"><path d="M0 2 H12 V10 H0 Z M1 3 L6 7 L11 3 Z" fill-rule="evenodd"/></svg>
        meridelhort@fernmail.example
      </li>
      <li>
        <svg viewBox="0 0 12 12" aria-hidden="true"><path d="M6 0 A6 6 0 1 0 6 12 A6 6 0 1 0 6 0 Z M6 1.5 C4.5 3 4.5 9 6 10.5 C7.5 9 7.5 3 6 1.5 Z M1.2 5.4 H10.8 V6.6 H1.2 Z" fill-rule="evenodd"/></svg>
        www.meridelhorticulture.example.au
      </li>
    </ul>
  </section>

</main>
</body>
</html>
```